Independent Midwife for a positive birth experience needs a vibrant, and elegant business card/logo

I need a business card design with a logo. The logo I would like to be able to use on my website (www.midwifeorlaith.com) next to my name.
Therefore the design of the card and logo should suit the colours and design of the website. The title of the website and company is "Orlaith Denby Marsworth, Midwife" but I'd like to have the business card title to be "Orlaith Denby Marsworth - Independent Midwife" in bold letters, same script font as in my website.

I provide gold standard midwifery services, one-to-one tailored care, continuity of care throughout the entire pregnancy (antenatal care), the birth and after the birth (postnatal care), home birth, water birth, breast-feeding support, and birth preparation workshops. I also am certified and offer complementary therapies: pregnancy reflexology, rebozo techniques for optimal baby positioning.

The design should incorporate similar colours and style as the website and the "Orlaith Denby Marsworth - Independent Midwife" on the card should include the same font as in the title of the website, however, in bold. The front of the card should have a logo, title and contact information (phone number 071592604, email orlaith.marsworth@quillpost.com, website address www.midwifeorlaith.com).
The back of the card to include the services I offer.

The logo: use of colour purple (varying shades), should communicate communicate warmth, kindness, compassion. It should convey that I'm a midwife who believes in fostering a trusting relationship with my clients and to provide them with a positive pregnancy and birth experience.

Target Market(s)

Pregnant women or women who are looking to book a private midwife for better birth experience and outcome

Industry/Entity Type

Baby

Contact Information for Business Card

Name and Title on front side together with contact details
The reverse side should have services/packages offered

Font styles to use
Script
Other font styles liked:
• similar script as in my website for name and title, and easy to read font for the rest of the words

Colors
b768aa
a54599
d2a4cc
ffffff

Requirements
Must have
• same font as title of website, but slightly bolder.
• similar design, colours, patterns as in website.
• Also include a gold accent colour somewhere in the design please.
Nice to have
• perhaps a logo of pregnant belly in profile or newborn baby icon

```html
<!DOCTYPE html>
<html lang="en">
<head>
<meta charset="utf-8">
<title>Orlaith Denby Marsworth - Independent Midwife · Business Card</title>
<link rel="stylesheet" href="https://fonts.googleapis.com/css2?family=Cookie&family=Lato:wght@400;700&display=swap">
<style>
  :root {
    --stage: #000000;
    --plum: #a3469a;
    --plum-light: #a84d9e;
    --plum-line: #b161a6;
    --paper-top: #ffffff;
    --paper-bottom: #cfcfcf;
    --white: #ffffff;
    --script: "Cookie", cursive;
    --sans: "Lato", Arial, sans-serif;
  }
  * { margin: 0; padding: 0; box-sizing: border-box; }
  html, body { width: 1200px; height: 900px; overflow: hidden; background: var(--stage); }
  .canvas { position: relative; width: 1200px; height: 900px; background: var(--stage); }

  .card { position: absolute; width: 592px; height: 337px; overflow: hidden; }

  /* Front */
  .card--front { left: 99px; top: 98px; }
  .front__head {
    position: absolute; left: 0; top: 0; width: 100%; height: 222px;
    background: linear-gradient(160deg, var(--paper-top) 15%, var(--paper-bottom) 100%);
  }
  .brand-ring { position: absolute; }
  .front__ring { left: 255px; top: 80px; width: 82px; height: 82px; }
  .brand-title {
    position: absolute; left: 0; width: 100%; text-align: center;
    font-family: var(--script); font-weight: 400; white-space: nowrap;
  }
  .front__title { top: 158px; font-size: 27px; color: var(--plum); }
  .front__foot {
    position: absolute; left: 0; top: 222px; width: 100%; height: 115px;
    background: var(--plum);
  }
  .front__divider {
    position: absolute; left: 296px; top: 0; width: 1px; height: 100%;
    background: var(--plum-line);
  }
  .holder { position: absolute; right: 325px; top: 23px; text-align: right; color: var(--white); font-family: var(--sans); }
  .holder__name { font-size: 18px; font-weight: 700; letter-spacing: 0.2px; }
  .holder__role { font-size: 11px; margin-top: 3px; }
  .contacts { position: absolute; left: 316px; top: 23px; list-style: none; font-family: var(--sans); color: var(--white); font-size: 12.5px; }
  .contacts li { display: flex; align-items: center; height: 21px; }
  .contacts svg { width: 13px; height: 13px; margin-right: 11px; flex: none; }

  /* Back */
  .card--back { left: 441px; top: 476px; background: var(--plum); }
  .back__band {
    position: absolute; left: 0; top: 222px; width: 100%; height: 115px;
    background: var(--plum-light);
  }
  .back__ring { left: 261px; top: 77px; width: 71px; height: 71px; }
  .back__title { top: 160px; font-size: 29px; color: var(--white); }
  .services {
    position: absolute; left: 0; top: 248px; width: 100%; text-align: center;
    font-family: var(--sans); font-size: 10px; color: var(--white); text-transform: uppercase;
    letter-spacing: 0.1px;
  }
  .services p { height: 19px; line-height: 14px; word-spacing: 1px; }
  .services .sep { margin: 0 8px; }
</style>
</head>
<body>
<main class="canvas">

  <section class="card card--front" aria-label="Business card front">
    <div class="front__head">
      <svg class="brand-ring front__ring" viewBox="0 0 82 82" aria-hidden="true">
        <circle cx="41" cy="41" r="38.5" fill="none" stroke="var(--plum)" stroke-width="4"/>
      </svg>
      <h1 class="brand-title front__title">Orlaith Denby Marsworth - Independent Midwife</h1>
    </div>
    <div class="front__foot">
      <div class="front__divider"></div>
      <div class="holder">
        <div class="holder__name">YOUR NAME</div>
        <div class="holder__role">DESIGNATION</div>
      </div>
      <ul class="contacts">
        <li>
          <svg viewBox="0 0 14 14" aria-label="Phone"><path d="M1 5c0-2 3-3 6-3s6 1 6 3l-1 1.5-2.5-1V4.5h-5v1L2 6.5z M3 7h8l1 5H2z" fill="var(--white)"/></svg>
          071592604
        </li>
        <li>
          <svg viewBox="0 0 14 14" aria-label="Email"><rect x="1" y="3" width="12" height="8.5" fill="var(--white)"/><path d="M1 3l6 5 6-5" fill="none" stroke="var(--plum)" stroke-width="1.2"/></svg>
          orlaith.marsworth@quillpost.com
        </li>
        <li>
          <svg viewBox="0 0 14 14" aria-label="Website"><g fill="none" stroke="var(--white)" stroke-width="1.6" stroke-linecap="round"><path d="M6 8.5l-1.8 1.8a1.8 1.8 0 0 1-2.5-2.5L3.5 6"/><path d="M8 5.5l1.8-1.8a1.8 1.8 0 0 1 2.5 2.5L10.5 8"/><path d="M5.5 8.5l3-3"/></g></svg>
          www.midwifeorlaith.com
        </li>
      </ul>
    </div>
  </section>

  <section class="card card--back" aria-label="Business card back">
    <div class="back__band"></div>
    <svg class="brand-ring back__ring" viewBox="0 0 71 71" aria-hidden="true">
      <circle cx="35.5" cy="35.5" r="33" fill="none" stroke="var(--white)" stroke-width="4"/>
    </svg>
    <h2 class="brand-title back__title">Orlaith Denby Marsworth - Independent Midwife</h2>
    <div class="services">
      <p>One-to-one tailored care<span class="sep">|</span>Antenatal care<span class="sep">|</span>Postnatal care<span class="sep">|</span>Home birth<span class="sep">|</span>Water birth</p>
      <p>Breast-feeding support<span class="sep">|</span>Birth preparation workshops<span class="sep">|</span>Pregnancy reflexology</p>
      <p>Rebozo techniques for optimal baby positioning</p>
    </div>
  </section>

</main>
</body>
</html>
```